International Medical travel company needs professional card

We just purchased a logo through sketch nest, and now need a business card. We contract with Middle Eastern governments to bring patients who need complex medical care to the U.S. for treatment. We will upload logo. Titles, names, contact info, etc. needs to be in English on one side, Arabic on the other

Target Market(s)

Health administrators, professionals

Industry/Entity Type

Health Care

Contact Information for Business Card

logo on each side. Usual name/title/contact info

Font styles to use
Serif
Sans Serif

Colors
0255a3

Requirements
Must have
• English one side, Arabic the other

```html
<!DOCTYPE html>
<html lang="en">
<head>
<meta charset="utf-8">
<title>Meridian Care – Business Card</title>
<link rel="stylesheet" href="https://fonts.googleapis.com/css2?family=EB+Garamond:wght@400;600;700&family=Amiri:wght@400;700&display=swap">
<style>
  :root{
    --backdrop:#262626;
    --card:#fbfbfb;
    --gold:#b39a2b;
    --gold-light:#d8c56a;
    --blue:#0255a3;
    --ink:#4a4a4a;
    --map:#e4e5ee;
  }
  *{box-sizing:border-box;margin:0;padding:0}
  html,body{width:1200px;height:873px;overflow:hidden;background:var(--backdrop)}
  .stage{position:relative;width:1200px;height:873px;display:flex;gap:40px;align-items:center;justify-content:center}
  .card{position:relative;width:540px;height:309px;background:var(--card);border-radius:16px;overflow:hidden;font-family:"EB Garamond",serif;color:var(--ink)}
  .world-map{position:absolute;left:60px;top:110px;width:440px;height:170px;border-radius:40px;
    background:radial-gradient(ellipse at 40% 50%,var(--map) 0%,rgba(228,229,238,.5) 55%,rgba(251,251,251,0) 75%)}
  .brand{position:absolute;left:0;right:0;top:40px;display:flex;align-items:center;justify-content:center;gap:12px}
  .brand-square{width:46px;height:46px;background:var(--gold)}
  .brand-name{font-family:"EB Garamond",serif;font-weight:600;font-size:38px;letter-spacing:2px;color:var(--gold);text-transform:uppercase}
  .divider{position:absolute;left:272px;top:148px;width:2px;height:110px;background:linear-gradient(var(--card),var(--gold-light) 40%,var(--gold) 70%,var(--card))}
  .identity{position:absolute;right:282px;top:150px;text-align:right}
  .person-name{font-size:22px;font-weight:600;color:var(--gold);line-height:1.1}
  .person-title{font-size:17px;color:var(--ink)}
  .address{margin-top:18px;font-size:16px;font-weight:700;color:var(--gold);line-height:1.4}
  .contacts{position:absolute;left:292px;top:148px;list-style:none}
  .contacts li{display:flex;align-items:center;gap:12px;font-size:15px;height:27px}
  .contacts svg{width:16px;height:16px;fill:var(--blue)}
  .card-arabic .identity{font-family:"Amiri",serif;direction:rtl}
  .card-arabic .person-name{font-size:23px}
  .card-arabic .person-title{font-size:15px}
  .card-arabic .address{font-size:15px;line-height:1.5}
</style>
</head>
<body>
<main class="stage">
  <section class="card card-arabic" lang="ar">
    <div class="world-map" role="img" aria-label="Dotted world map background"></div>
    <div class="brand" lang="en"><span class="brand-square"></span><span class="brand-name">Meridian Care</span></div>
    <div class="identity">
      <p class="person-name">دانيال رييس</p>
      <p class="person-title">المالك / المؤسس</p>
      <p class="address">4870 طريق ألدر ، جناح B<br>سان أنطونيو ، تكساس 78240</p>
    </div>
    <span class="divider"></span>
    <ul class="contacts" lang="en">
      <li><svg viewBox="0 0 16 16"><path d="M2 5c0-2 2-3 6-3s6 1 6 3l-3 1-1-2H6L5 6zM4 8h8l2 6H2z"/></svg>210-555-0180</li>
      <li><svg viewBox="0 0 16 16"><path d="M4 1h8v14H4zM5.5 3v9h5V3z"/></svg>210-555-0127</li>
      <li><svg viewBox="0 0 16 16"><path d="M4 1h8v4H4zM1 6h14v6h-3v3H4v-3H1zM5 10v4h6v-4z"/></svg>210-555-0193</li>
      <li><svg viewBox="0 0 16 16"><path d="M1 3h14v10H1zM2 4l6 5 6-5z"/></svg>info@meridiancare.com</li>
    </ul>
  </section>

  <section class="card card-english">
    <div class="world-map" role="img" aria-label="Dotted world map background"></div>
    <div class="brand"><span class="brand-square"></span><span class="brand-name">Meridian Care</span></div>
    <div class="identity">
      <p class="person-name">Daniel Reyes</p>
      <p class="person-title">Owner / Founder</p>
      <p class="address">4870 Alder Rd., Suite B.<br>San Antonio, TX. 78240</p>
    </div>
    <span class="divider"></span>
    <ul class="contacts">
      <li><svg viewBox="0 0 16 16"><path d="M2 5c0-2 2-3 6-3s6 1 6 3l-3 1-1-2H6L5 6zM4 8h8l2 6H2z"/></svg>210-555-0180</li>
      <li><svg viewBox="0 0 16 16"><path d="M4 1h8v14H4zM5.5 3v9h5V3z"/></svg>210-555-0127</li>
      <li><svg viewBox="0 0 16 16"><path d="M4 1h8v4H4zM1 6h14v6h-3v3H4v-3H1zM5 10v4h6v-4z"/></svg>210-555-0193</li>
      <li><svg viewBox="0 0 16 16"><path d="M1 3h14v10H1zM2 4l6 5 6-5z"/></svg>info@meridiancare.com</li>
    </ul>
  </section>
</main>
</body>
</html>
```